Pebble Brook Cafe Take Out Menu

We serve coffee and tea made from our very own reverse osmosis water. Serve sandwiches, soups, pastry and more. Christian company! Want a to go menu so it needs to be condensed from one I sent you.

Target Market(s)

Portales and Roosevelt County NM

Industry/Entity Type

Coffee Shop

```html
<!DOCTYPE html>
<html lang="en">
<head>
<meta charset="utf-8">
<title>Take Out Menu – Salads, Soups, Sides, Wraps</title>
<link rel="stylesheet" href="https://fonts.googleapis.com/css2?family=Archivo+Narrow:wght@400;500&family=Lobster+Two:wght@700&family=Josefin+Sans:wght@400;600&display=swap">
<style>
  :root {
    --green: #3b9a3c;
    --navy: #1f3b70;
    --red: #d2382c;
    --ink: #1d1d1d;
    --paper: #ffffff;
  }
  * { margin: 0; padding: 0; box-sizing: border-box; }
  html, body { width: 778px; height: 1200px; overflow: hidden; background: var(--paper); }
  .menu {
    position: relative; width: 778px; height: 1200px; overflow: hidden;
    font-family: "Archivo Narrow", "Arial Narrow", sans-serif; color: var(--ink);
    font-size: 20px; line-height: 24px;
  }
  .abs { position: absolute; }
  .salads-frame {
    left: 24px; top: 10px; width: 730px; height: 498px;
    border: 4px dotted var(--green); border-radius: 28px;
  }
  .section-title {
    font-family: "Josefin Sans", sans-serif; font-weight: 400; letter-spacing: 10px;
    color: var(--navy); text-align: center;
  }
  .salads-title { left: 0; width: 778px; top: 40px; font-size: 50px; line-height: 54px; padding-left: 10px; }
  .swoosh { left: 249px; width: 280px; }
  .item-name {
    font-family: "Lobster Two", cursive; font-weight: 700; color: var(--green);
    font-size: 28px; line-height: 32px;
  }
  .salad { text-align: center; }
  .col-left { left: 40px; width: 350px; }
  .col-right { left: 412px; width: 330px; }
  .soups-badge { left: 18px; top: 530px; width: 150px; height: 50px; }
  .soups-info { left: 190px; top: 524px; width: 560px; text-align: center; }
  .rule { height: 2px; background: var(--navy); }
  .sides-head { left: 20px; top: 612px; width: 360px; height: 40px; }
  .sides-title { left: 90px; top: 614px; width: 200px; font-size: 40px; line-height: 40px; color: var(--red); letter-spacing: 8px; }
  .side { left: 34px; width: 370px; line-height: 28px; }
  .side .item-name { color: var(--red); font-size: 25px; line-height: 30px; }
  .side-text { line-height: 26px; }
  .inline-name { font-family: "Lobster Two", cursive; font-weight: 700; color: var(--red); font-size: 25px; line-height: 1; }
  .wraps-frame {
    left: 423px; top: 608px; width: 334px; height: 441px;
    border: 3px dashed var(--navy); border-radius: 18px;
  }
  .wraps { left: 432px; top: 620px; width: 316px; text-align: center; }
  .wraps-title { font-size: 40px; line-height: 42px; color: var(--red); letter-spacing: 8px; }
  .wraps-price { font-family: "Josefin Sans", sans-serif; color: var(--red); font-size: 22px; line-height: 28px; }
  .wrap-key { font-family: "Lobster Two", cursive; font-weight: 700; color: var(--red); font-size: 24px; line-height: 1; }
  .wraps p { margin-top: 4px; line-height: 26px; }
  .extras-band { left: 0; top: 1114px; width: 34px; height: 86px; background: var(--red); }
  .extras-label {
    left: 0; top: 1114px; width: 34px; height: 86px; color: var(--paper);
    font-family: "Josefin Sans", sans-serif; font-size: 16px; letter-spacing: 3px;
    writing-mode: vertical-rl; transform: rotate(180deg); text-align: center; line-height: 34px;
  }
  .extras-col { top: 1120px; font-size: 20px; line-height: 25px; }
</style>
</head>
<body>
<main class="menu">

  <div class="abs salads-frame"></div>
  <svg class="abs swoosh" style="top:22px" width="280" height="22" viewBox="0 0 280 22" aria-hidden="true">
    <path d="M8 18 Q140 -5 272 18" fill="none" stroke="var(--green)" stroke-width="3"/>
  </svg>
  <h1 class="abs section-title salads-title">SALADS</h1>
  <svg class="abs swoosh" style="top:94px" width="280" height="22" viewBox="0 0 280 22" aria-hidden="true">
    <path d="M8 4 Q140 27 272 4" fill="none" stroke="var(--green)" stroke-width="3"/>
  </svg>

  <article class="abs salad col-left" style="top:124px">
    <h2 class="item-name">Chef Salad</h2>
    <p>A generous bed of mixed green lettuce with ham, grilled chicken, bacon, shredded cheese, boiled egg, tomatoes, onion, cucumber, croûtons and your choice of dressing. $7.00</p>
  </article>
  <article class="abs salad col-left" style="top:286px">
    <h2 class="item-name">Grilled Chicken Salad</h2>
    <p>A generous bed of mixed green lettuce, grilled chicken, shredded cheese, tomatoes, onion, cucumbers, croûtons and your choice of dressing. $6.75</p>
  </article>
  <article class="abs salad col-right" style="top:124px">
    <h2 class="item-name">Pecan Chicken Salad</h2>
    <p>A generous portion of fresh green lettuce mix with a large scoop of our fresh homemade pecan chicken salad topped with tomatoes. $6.50</p>
  </article>
  <article class="abs salad col-right" style="top:266px">
    <h2 class="item-name">Tuna Salad</h2>
    <p>A generous portion of fresh green lettuce mix with a large scoop of our fresh homemade tuna salad topped with tomatoes. $6.50</p>
  </article>
  <article class="abs salad" style="left:30px;width:718px;top:440px">
    <h2 class="item-name">Side Salad</h2>
    <p>A small lettuce and tomato side salad served with your choice of dressing. $3.00</p>
  </article>

  <svg class="abs soups-badge" viewBox="0 0 150 50" aria-hidden="true">
    <path d="M4 4 H146 Q140 44 75 47 Q10 44 4 4 Z" fill="var(--navy)"/>
    <text x="75" y="30" text-anchor="middle" font-family="Josefin Sans, sans-serif" font-size="24" letter-spacing="5" fill="#fff">SOUPS</text>
  </svg>
  <div class="abs soups-info">
    <p>Ask server for daily soup options</p>
    <p>Available In 3 Sizes SM. $2.49 LG. $3.99 FAMILY $12.99</p>
  </div>
  <div class="abs rule" style="left:18px;top:586px;width:740px"></div>

  <svg class="abs sides-head" viewBox="0 0 360 40" aria-hidden="true">
    <line x1="0" y1="20" x2="62" y2="20" stroke="var(--red)" stroke-width="2"/>
    <line x1="298" y1="20" x2="360" y2="20" stroke="var(--red)" stroke-width="2"/>
    <circle cx="66" cy="20" r="3" fill="var(--red)"/>
    <circle cx="294" cy="20" r="3" fill="var(--red)"/>
  </svg>
  <h2 class="abs section-title sides-title">SIDES</h2>

  <article class="abs side" style="top:664px">
    <h3 class="item-name">Guacamole &amp; Chips</h3>
    <p class="side-text">Made fresh daily and served with tortilla chips. Small $3.50 Large $4.95</p>
  </article>
  <p class="abs side" style="top:752px"><span class="inline-name">Pasta Salad</span> Small $1.25<br>Medium....$1.75 Large$2.25</p>
  <p class="abs side" style="top:820px"><span class="inline-name">Coleslaw</span> Small $1.25<br>Medium $1.75 Large $2.25</p>
  <p class="abs side" style="top:888px"><span class="inline-name">Potato Salad</span> Small $1.25<br>Medium....$1.75 Large $2.25</p>
  <p class="abs side" style="top:956px"><span class="inline-name">Fresh Fruit Cup</span> Fresh fruit as<br>available and in season! $2.50</p>

  <div class="abs wraps-frame"></div>
  <section class="abs wraps">
    <h2 class="section-title wraps-title">WRAPS</h2>
    <p class="wraps-price">~ $6.50 ~</p>
    <p>Choose From The Following</p>
    <p><span class="wrap-key">Tortilla</span> Tomato Basil, Jalapeño Cheddar, Garlic Herb, Spinach</p>
    <p><span class="wrap-key">Meat</span> Turkey, ham or roast beef Cheese: cheddar, pepper jack, Swiss or American</p>
    <p><span class="wrap-key">Sauce</span> Mayo, Ranch, Honey Mustard, Mustard</p>
    <p><span class="wrap-key">Veggies</span> lettuce, tomato, onion, cucumber, ranch dressing Served with chips.</p>
  </section>

  <div class="abs rule" style="left:0;top:1112px;width:778px"></div>
  <div class="abs extras-band"></div>
  <div class="abs extras-label">EXTRAS</div>
  <div class="abs extras-col" style="left:52px">Gluten free bread 2.00<br>Cheese .50<br>Meat 1.50</div>
  <div class="abs extras-col" style="left:312px">Green chili .50<br>Boiled egg 1.00<br>Extra dressing .75</div>
  <div class="abs extras-col" style="left:540px;width:220px;text-align:center">Guacamole<br>(mini on side or on<br>sandwich/salad) 1.00</div>

</main>
</body>
</html>
```